Business Card for TOV

We need a Corporate style business card for a new Industrial recycling company based in Australia. We recycle industrial products from Mining companies, power stations and other large industry all around the country.

We want the card to represent a modern, innovative professional company that is an industry leader.

We want the card to be double sided. I think with the logo centred by itself on one side and the text displayed with all our details on the other side.

(or you could put the persons name with the job title on the side with the logo?? I'll leave that up to your creative sides)

Open to how you divide and place the information on the one side of the card.

I think the persons name and the title should have its own place. The rest of the information can be placed as you think is best and then I will provide feedback as to what I think works best.

I have attached the logo file so you can add that to the one side. Whether you use it in a smaller form on the second side too is an option but I'll leave that up to you initially?

Information required on the card is as follows

Dermot Halloran
Director

0438 972 506

dermot@tovq.com.au

Po Box 782
Brindle ACT 2694

www.tovq.com.au

ACN 582 917 306 (This can be in very small print and can be in the bottom corner of the card or somewhere not very prominent

Wanted to thank everyone for their submissions. 

We were really torn on about 5 designs in the end.

We decided to go with the first one we liked.

We have another company that is going to need logo and business card design in the coming weeks.

I will save your designer ID's so I can invite you all to that project. too!

Thanks again and all the best

Dermot

Target Market(s)

Corporate and medium to large business clients

Industry/Entity Type

Industrial

```html
<!DOCTYPE html>
<html lang="en">
<head>
<meta charset="utf-8">
<title>TOV Business Card – Front and Back</title>
<link rel="stylesheet" href="https://fonts.googleapis.com/css2?family=Open+Sans:wght@400;600;700&family=Michroma&family=Cormorant+Garamond:wght@600&display=swap">
<style>
  :root {
    --stage: #e9e7e4;
    --card-white: #ffffff;
    --card-fade: #e6e6e6;
    --ink-dark: #2b2b2b;
    --band: #2f2f2f;
    --band-deep: #262626;
    --accent-green: #6fbf2a;
    --logo-teal: #2f6f86;
    --text-light: #c9c9c9;
    --text-white: #f4f4f4;
    --ghost: #d6dcd6;
  }
  * { margin: 0; padding: 0; box-sizing: border-box; }
  html, body { width: 1200px; height: 900px; overflow: hidden; }
  body {
    background: var(--stage);
    font-family: "Open Sans", Arial, sans-serif;
    display: flex;
    flex-direction: column;
    align-items: center;
    justify-content: center;
    gap: 40px;
  }
  .card {
    width: 640px;
    height: 390px;
    position: relative;
    overflow: hidden;
    box-shadow: 0 6px 18px rgba(0,0,0,0.18);
  }

  /* Front */
  .card-front {
    background: linear-gradient(180deg, var(--card-white) 0%, var(--card-white) 45%, var(--card-fade) 100%);
    display: flex;
    align-items: center;
    justify-content: center;
  }
  .brand {
    display: flex;
    align-items: center;
    gap: 16px;
  }
  .brand-dot {
    width: 58px; height: 58px;
    border-radius: 50%;
    background: var(--accent-green);
    flex: none;
  }
  .brand-name {
    font-weight: 700;
    font-size: 26px;
    line-height: 1.1;
    letter-spacing: 1px;
    text-transform: uppercase;
    color: var(--logo-teal);
  }

  /* Back */
  .card-back { background: linear-gradient(180deg, var(--card-white) 0%, #f1f1f1 100%); }
  .brand-ghost {
    position: absolute;
    left: 150px; top: 40px;
    gap: 14px;
  }
  .brand-ghost .brand-dot { width: 70px; height: 70px; background: var(--ghost); }
  .brand-ghost .brand-name { color: var(--ghost); font-size: 27px; }

  .person {
    position: absolute;
    left: 36px; top: 172px;
  }
  .person-name {
    font-family: "Michroma", Arial, sans-serif;
    font-variant: small-caps;
    font-size: 24px;
    letter-spacing: 2px;
    color: var(--ink-dark);
  }
  .person-title {
    font-family: "Cormorant Garamond", Georgia, serif;
    font-weight: 600;
    font-size: 20px;
    color: var(--ink-dark);
    margin-top: -4px;
  }

  .details-band {
    position: absolute;
    left: 0; right: 0; bottom: 0;
    height: 160px;
    background: linear-gradient(180deg, var(--band) 0%, var(--band-deep) 100%);
    border-top: 4px solid var(--accent-green);
  }
  .detail {
    position: absolute;
    display: flex;
    align-items: center;
    gap: 12px;
    font-size: 19px;
    color: var(--text-light);
    white-space: nowrap;
  }
  .detail svg { width: 20px; height: 20px; flex: none; }
  .detail-phone   { left: 36px;  top: 48px; }
  .detail-email   { left: 250px; top: 48px; font-size: 18px; }
  .detail-address { left: 36px;  top: 96px; }
  .detail-web     { left: 440px; top: 8px; font-size: 17px; }
  .company-number {
    position: absolute;
    right: 24px; top: 52px;
    font-size: 15px;
    color: var(--text-white);
  }
</style>
</head>
<body>

  <section class="card card-front" aria-label="Card front">
    <div class="brand">
      <span class="brand-dot"></span>
      <span class="brand-name">Tovara<br>Industrial Recovery</span>
    </div>
  </section>

  <section class="card card-back" aria-label="Card back">
    <div class="brand brand-ghost">
      <span class="brand-dot"></span>
      <span class="brand-name">Tovara<br>Industrial Recovery</span>
    </div>

    <div class="person">
      <p class="person-name">Dermot Halloran</p>
      <p class="person-title">Director</p>
    </div>

    <div class="details-band">
      <p class="detail detail-web">
        <svg viewBox="0 0 20 20" fill="none" stroke="#c9c9c9" stroke-width="1.4"><circle cx="10" cy="10" r="8"/><ellipse cx="10" cy="10" rx="3.5" ry="8"/><line x1="2" y1="10" x2="18" y2="10"/></svg>
        www.tovq.com.au
      </p>
      <p class="detail detail-phone">
        <svg viewBox="0 0 20 20" fill="none" stroke="#c9c9c9" stroke-width="1.5"><rect x="5" y="1.5" width="10" height="17" rx="2"/><line x1="8.5" y1="15.5" x2="11.5" y2="15.5"/></svg>
        0438 972 506
      </p>
      <p class="detail detail-email">
        <svg viewBox="0 0 20 20" fill="none" stroke="#c9c9c9" stroke-width="1.5"><rect x="2" y="4.5" width="16" height="11"/><polyline points="2,4.5 10,11 18,4.5"/></svg>
        dermot@tovq.com.au
      </p>
      <p class="detail detail-address">
        <svg viewBox="0 0 20 20" fill="#c9c9c9"><rect x="5" y="3" width="10" height="15"/><rect x="7" y="5" width="2" height="2" fill="#2f2f2f"/><rect x="11" y="5" width="2" height="2" fill="#2f2f2f"/><rect x="7" y="9" width="2" height="2" fill="#2f2f2f"/><rect x="11" y="9" width="2" height="2" fill="#2f2f2f"/><rect x="9" y="14" width="2" height="4" fill="#2f2f2f"/><rect x="3" y="17.5" width="14" height="1.5"/></svg>
        Po Box 782, Brindle ACT 2694
      </p>
      <p class="company-number">ACN 582 917 306</p>
    </div>
  </section>

</body>
</html>
```